Asia based real estate financing firm needs and AWESOME design for a biz card -Harbor Lending Circle

Looking for a stylish, & corporate-looking business card for a real estate financing brokerage firm in Asia, offering global mortgage loans. I uploaded our current logos. We would like to add a splash of color (perhaps the house icon) or any other suggestions are open. For the winning designer, we have a lot of work! Thanks and best of luck!

Target Market(s)

Real estate investors globally. We want to look more like a BANK and NOT a real estate company. Please don't play up on a "house" design.

Industry/Entity Type

Banking

Contact Information for Business Card

Harbor Lending Circle
Peter Wilks
Co-Founder | Partner

14 Cassia Lane, Suite 310
Singapore 047219
www.hlc-example.asia
peterwilks@hlc-example.asia
+65 555-0142
WeChat: peterwilks

Colors

Designer to choose colors to be used in the design.

Requirements
Must have
• Must have the standard business requirements for a card; name, address, email, etc
• Can be horizontal or vertical.
Nice to have
• It would be great to see some sort of variation to the logo with a pop of color. Red is good as we're in Asia, however, other options work as well.
• Our tag line is - Borderless mortgages. It doesn't have to be on the card but might be nice.
• I'd like to start seeing our tagline within the cards as well. - Borderless mortgages.
• Also, please add our location. The location for this card is Singapore so perhaps it can be highlighted or emphasised in some way.
• Singapore | Hong Kong | Shanghai | Manila
• As we will soon open an office in Shanghai, having an option for both languages would be great.
Should not have
• I'm exceited and open to your creativity ... knock it out of the park!

```html
<!DOCTYPE html>
<html lang="en">
<head>
<meta charset="utf-8">
<title>Harbor Lending Circle – Business Card Set</title>
<link rel="stylesheet" href="https://fonts.googleapis.com/css2?family=Lora:wght@400;600;700&display=swap">
<style>
  :root {
    --page: #f7f3f3;
    --paper: #ffffff;
    --ink: #1f2836;
    --black: #0d0d0d;
    --navy: #252b37;
    --blue: #2461b0;
    --red: #bf2328;
    --on-dark: #ffffff;
  }
  * { box-sizing: border-box; margin: 0; padding: 0; }
  html, body { width: 968px; height: 1200px; overflow: hidden; background: var(--page); }
  body { position: relative; font-family: "Lora", Georgia, serif; color: var(--ink); }

  .card { position: absolute; width: 436px; height: 262px; }
  .card-front { left: 36px; display: flex; flex-direction: column; align-items: center; justify-content: center; gap: 12px; }
  .card-back { left: 496px; width: 434px; background: var(--paper); }

  .row-1 { top: 44px; }
  .row-2 { top: 328px; }
  .row-3 { top: 618px; }
  .row-4 { top: 907px; }

  .front-black { background: var(--black); }
  .front-navy { background: var(--navy); }
  .front-blue { background: var(--blue); }
  .front-red { background: var(--red); }

  .brand-mark { width: 12px; height: 12px; background: var(--on-dark); }
  .brand-name {
    color: var(--on-dark);
    font-weight: 400;
    font-size: 21px;
    letter-spacing: 2.5px;
    text-transform: uppercase;
    text-align: center;
  }

  .back-brand {
    position: absolute; left: 40px; top: 0; width: 160px; height: 100%;
    display: flex; align-items: center; justify-content: center; text-align: center;
    color: var(--ink); font-weight: 600; font-size: 20px; line-height: 1.25;
    letter-spacing: 1.5px; text-transform: uppercase;
  }
  .back-brand.is-large { font-size: 24px; }

  .back-wordmark {
    position: absolute; left: 49px; top: 46px;
    color: var(--ink); font-weight: 700; font-size: 14px; line-height: 19px;
    letter-spacing: 1px; text-transform: uppercase;
  }
  .back-web { position: absolute; left: 49px; top: 212px; font-size: 8px; font-weight: 600; }

  .contact { position: absolute; left: 246px; top: 0; font-size: 8.5px; line-height: 14.5px; }
  .contact-name { position: absolute; top: 45px; font-size: 16px; font-weight: 600; letter-spacing: 0.5px; white-space: nowrap; }
  .contact-role { position: absolute; top: 68px; font-weight: 600; letter-spacing: 0.5px; white-space: nowrap; }
  .contact-address { position: absolute; top: 109px; white-space: nowrap; }
  .contact-lines { position: absolute; top: 175px; white-space: nowrap; }
  .contact-lines b { font-weight: 700; }
</style>
</head>
<body>

  <!-- Row 1 -->
  <section class="card card-front front-black row-1">
    <span class="brand-mark"></span>
    <p class="brand-name">Harbor Lending Circle</p>
  </section>
  <section class="card card-back row-1">
    <p class="back-brand">Harbor<br>Lending<br>Circle</p>
    <div class="contact">
      <p class="contact-name">Peter Wilks</p>
      <p class="contact-role">Co-Founder &amp; Partner</p>
      <p class="contact-address">14 Cassia Lane,<br>Suite 310 Singapore<br>047219</p>
      <p class="contact-lines"><b>T :</b> +65 555-0142<br><b>WeChat:</b> peterwilks<br><b>E :</b> peterwilks@hlc-example.asia<br><b>W:</b> hlc-example.asia</p>
    </div>
  </section>

  <!-- Row 2 -->
  <section class="card card-front front-navy row-2">
    <span class="brand-mark"></span>
    <p class="brand-name">Harbor Lending Circle</p>
  </section>
  <section class="card card-back row-2">
    <p class="back-brand is-large">Harbor<br>Lending<br>Circle</p>
    <div class="contact">
      <p class="contact-name">Peter Wilks</p>
      <p class="contact-role">Co-Founder &amp; Partner</p>
      <p class="contact-address">14 Cassia Lane,<br>Suite 310 Singapore<br>047219</p>
      <p class="contact-lines"><b>T :</b> +65 555-0142<br><b>WeChat:</b> peterwilks<br><b>E :</b> peterwilks@hlc-example.asia<br><b>W:</b> hlc-example.asia</p>
    </div>
  </section>

  <!-- Row 3 -->
  <section class="card card-front front-blue row-3">
    <span class="brand-mark"></span>
    <p class="brand-name">Harbor Lending Circle</p>
  </section>
  <section class="card card-back row-3">
    <p class="back-brand is-large">Harbor<br>Lending<br>Circle</p>
    <div class="contact">
      <p class="contact-name">Peter Wilks</p>
      <p class="contact-role">Co-Founder &amp; Partner</p>
      <p class="contact-address">14 Cassia Lane,<br>Suite 310 Singapore<br>047219</p>
      <p class="contact-lines"><b>T :</b> +65 555-0142<br><b>WeChat:</b> peterwilks<br><b>E :</b> peterwilks@hlc-example.asia<br><b>W:</b> hlc-example.asia</p>
    </div>
  </section>

  <!-- Row 4 -->
  <section class="card card-front front-red row-4">
    <span class="brand-mark"></span>
    <p class="brand-name">Harbor Lending Circle</p>
  </section>
  <section class="card card-back row-4">
    <p class="back-wordmark">Harbor<br>Lending<br>Circle</p>
    <p class="back-web">www.hlc-example.asia</p>
    <div class="contact">
      <p class="contact-name">Peter Wilks</p>
      <p class="contact-role">Co-Founder &amp; Partner</p>
      <p class="contact-address">14 Cassia Lane,<br>Suite 310 Singapore<br>047219</p>
      <p class="contact-lines"><b>T :</b> +65 555-0142<br><b>WeChat:</b> peterwilks<br><b>E :</b> peterwilks@hlc-example.asia</p>
    </div>
  </section>

</body>
</html>
```